Simple, High-Class Web Design Wanted - Motivational Speakers Site

1. Full Brief/Request & Specs outlined on following video -
http://clipvane-recorder.com/watch/tbWrkLmQyP

2. Use colours, images as you feel suits objective (we are happy to pay up to US$30 for any good images but must have licence/permission).

3. Layout probably similar to existing site - www.podiumvoicehub.com.au / http://podiumvoicehub.com.au/contact.php

4. Must Be Able to Coded for MOBILE-FRIENDLINESS & WordPress friendly Ideal.

5. This is the first, small job of many we/graphic design jobs. If suits, winning designer may be offered all future work direct.

Thanks & look forward to your design. Glen.

Target Market(s)

corporates - high end

Number of Pages Required

2 page

Font styles to use
Sans Serif

Requirements
Must have
• Classy professional look
Nice to have
• all in Video in brief
Should not have
• too many images / new images I haven't approved

```html
<!DOCTYPE html>
<html lang="en">
<head>
<meta charset="utf-8">
<title>Podium Voice Hub – Find The Perfect Speaker</title>
<link href="https://fonts.googleapis.com/css2?family=Open+Sans:wght@300;400;600;700&display=swap" rel="stylesheet">
<style>
:root{
  --blue:#4fa6dc;
  --blue-dark:#3a8fc6;
  --teal:#3dc1b1;
  --ink:#3d4a55;
  --muted:#6b7680;
  --line:#c9d0d6;
  --band-grey:#eef1f3;
  --footer:#2f3b48;
  --white:#ffffff;
}
*{box-sizing:border-box;margin:0;padding:0}
html,body{width:1200px;height:2512px;overflow:hidden;background:var(--white)}
body{font-family:"Open Sans",Arial,sans-serif;color:var(--ink);position:relative}

.hero{position:absolute;left:0;top:0;width:1200px;height:512px;
  background:linear-gradient(180deg,#5c6d7c 0%,#7d8d99 45%,#a6b2ba 75%,#c3ccd2 100%)}
.hero-title{position:absolute;left:48px;top:38px;color:var(--white);font-size:42px;line-height:56px;font-weight:600;white-space:nowrap}
.hero-sub{position:absolute;left:48px;top:98px;color:#e7eef3;font-size:38px;line-height:50px;font-weight:300;white-space:nowrap}
.hero-pitch{position:absolute;right:48px;top:282px;width:660px;color:var(--white);font-size:22px;line-height:34px}
.btn-outline{position:absolute;right:48px;top:392px;width:168px;height:44px;border:2px solid var(--blue);
  color:var(--white);font-size:14px;font-weight:600;display:flex;align-items:center;justify-content:center;gap:10px;letter-spacing:1px}

.video-band{position:absolute;left:0;top:512px;width:1200px;height:450px;background:var(--band-grey)}
.video-frame{position:absolute;left:264px;top:530px;width:696px;height:412px;background:#fff;border:1px solid #dde2e6;box-shadow:0 4px 14px rgba(0,0,0,.08)}
.video-still{position:absolute;left:10px;top:10px;width:674px;height:346px;
  background:linear-gradient(180deg,#e4e9ed 0%,#cfd8df 100%)}
.play{position:absolute;left:305px;top:128px}
.video-controls{position:absolute;left:10px;top:364px;width:674px;height:36px}
.btn-solid{position:absolute;display:flex;align-items:center;justify-content:center;gap:12px;color:var(--white);font-weight:600;white-space:nowrap}
.btn-event{left:500px;top:992px;width:440px;height:44px;background:var(--blue);font-size:16px}

.section-head{position:absolute;left:0;width:1200px;display:flex;align-items:center;justify-content:center;gap:28px}
.section-head span{font-size:40px;font-weight:400;color:var(--ink)}
.section-head i{display:block;width:400px;height:1px;background:var(--line)}
.about-head{top:1116px}
.note-head{top:1922px}
.copy{position:absolute;left:64px;width:1072px;font-size:18px;line-height:28px;color:var(--ink)}
.copy p{margin-bottom:26px}

.criteria-band{position:absolute;left:0;top:1448px;width:1200px;height:300px;background:var(--blue)}
.criteria{position:absolute;left:0;top:56px;width:1200px;text-align:center;color:var(--white);font-size:17px;font-weight:600;line-height:28px}
.criteria li{list-style:none;margin-bottom:22px}
.btn-form{left:516px;top:1718px;width:372px;height:44px;background:var(--teal);font-size:16px;letter-spacing:.5px}
.btn-form-left{left:104px;top:2280px;width:380px;height:44px;background:var(--teal);font-size:16px;letter-spacing:.5px}

.contact-line{position:absolute;left:520px;top:2290px;font-size:18px;color:var(--ink);white-space:nowrap}
.contact-line b{color:var(--blue);font-weight:600}

.footer{position:absolute;left:0;top:2380px;width:1200px;height:132px;background:var(--footer)}
.footer p{position:absolute;left:0;width:1200px;text-align:center;color:#b9c2ca;font-size:13px;line-height:20px}
.to-top{position:absolute;right:40px;top:2352px;width:52px;height:52px;background:var(--teal);display:flex;align-items:center;justify-content:center}
</style>
</head>
<body>

<header class="hero" role="img" aria-label="Boardroom conference table photograph in cool grey tones">
  <h1 class="hero-title">Find The Perfect Speaker For Your Next Event Here...</h1>
  <p class="hero-sub">free industry service</p>
  <p class="hero-pitch">Looking for a top motivational or guest speaker, MC, industry expert to "WOW" your next event? find them here</p>
  <div class="btn-outline">
    <svg width="14" height="14" viewBox="0 0 14 14"><circle cx="7" cy="7" r="6" fill="none" stroke="#4fa6dc" stroke-width="2"/><path d="M6 4l3 3-3 3" fill="none" stroke="#4fa6dc" stroke-width="2"/></svg>
    CONTACT
  </div>
</header>

<section class="video-band">
</section>
<div class="video-frame">
  <div class="video-still" role="img" aria-label="Video still of the speaker presenting the service">
    <svg class="play" width="64" height="64" viewBox="0 0 64 64"><circle cx="32" cy="32" r="30" fill="#3dc1b1" opacity=".9"/><path d="M25 18l22 14-22 14z" fill="#fff"/></svg>
  </div>
  <svg class="video-controls" viewBox="0 0 674 36">
    <circle cx="16" cy="18" r="8" fill="none" stroke="#3dc1b1" stroke-width="2"/>
    <circle cx="40" cy="18" r="8" fill="none" stroke="#3dc1b1" stroke-width="2"/>
    <circle cx="64" cy="18" r="8" fill="none" stroke="#3dc1b1" stroke-width="2"/>
    <rect x="84" y="16" width="560" height="4" fill="#dbe1e5"/>
    <rect x="84" y="16" width="150" height="4" fill="#3dc1b1"/>
    <circle cx="658" cy="18" r="8" fill="none" stroke="#3dc1b1" stroke-width="2"/>
  </svg>
</div>
<div class="btn-solid btn-event">I Want to Make our Event a Great Success
  <svg width="18" height="18" viewBox="0 0 18 18"><circle cx="9" cy="9" r="8" fill="none" stroke="#fff" stroke-width="2"/><path d="M7 5l4 4-4 4" fill="none" stroke="#fff" stroke-width="2"/></svg>
</div>

<div class="section-head about-head"><i></i><span>About</span><i></i></div>
<div class="copy" style="top:1216px">
  <p>Podium Voice Hub is a free industry service designed to help people looking for speakers save precious time and frustration in finding the most suitable/best speaker for their needs.</p>
  <p>Suggestions are given by Australian conference speaker Glen Harlow, who has presented around Australia for a number of years and is familiar with many of our top professional speakers, MCs as well as the leading speaker bureaus.</p>
  <p>If you would like a hand finding some good speaker options, simply send us the details of your event and the type of presenter you are ideally after, e.g.</p>
</div>

<section class="criteria-band">
  <ul class="criteria">
    <li>Type/Style – Motivational, Entertaining, Keynote/Workshop, MC etc</li>
    <li>Topic/Area – Team Building, Leadership, Inspiration, Health/Life Balance etc</li>
    <li>Approximate Budget - $1000, $3500, $5000, $7500+ etc</li>
    <li>Location - Sydney, Melbourne, Brisbane, Perth, Adelaide, Canberra etc</li>
  </ul>
</section>
<div class="btn-solid btn-form">COMPLETE ONLINE CONTACT FORM
  <svg width="18" height="18" viewBox="0 0 18 18"><circle cx="9" cy="9" r="8" fill="none" stroke="#fff" stroke-width="2"/><path d="M7 5l4 4-4 4" fill="none" stroke="#fff" stroke-width="2"/></svg>
</div>

<div class="copy" style="top:1790px">
  <p>and where we can, we will be happy to send you some speaker possibilities/ideas, trusted speakers bureaus or simply some thoughts on the best places for you to look. Regards Glen.</p>
</div>

<div class="section-head note-head"><i></i><span>Note</span><i></i></div>
<div class="copy" style="top:2022px;text-align:center">
  <p>Any information you provide will ONLY ever be used to help with your specific enquiry.</p>
  <p>Glen does not have any financial agreements with any individual speakers he recommends. He offers this service, as it only takes a few minutes of his time, helps promote other professional speakers and obviously keeps his own name out there in the industry.</p>
  <p>Please understand that while Glen tries to respond quickly, due to his own speaking/travel commitments it may take up to 24 hours.</p>
</div>

<div class="btn-solid btn-form-left">COMPLETE ONLINE CONTACT FORM
  <svg width="18" height="18" viewBox="0 0 18 18"><circle cx="9" cy="9" r="8" fill="none" stroke="#fff" stroke-width="2"/><path d="M7 5l4 4-4 4" fill="none" stroke="#fff" stroke-width="2"/></svg>
</div>
<p class="contact-line"><b>E-MAIL</b> suggestions@podiumvoicehub.com.au <b>PHONE</b> 1300 40 72 19</p>

<footer class="footer">
  <p style="top:44px">© 2015. All Rights Reserved www.podiumvoicehub.com.au PO Box 418 Kirribilli NSW 2061</p>
  <p style="top:66px">E-mail: suggestions@podiumvoicehub.com.au Phone: 1300 40 72 19</p>
</footer>
<div class="to-top">
  <svg width="22" height="22" viewBox="0 0 22 22"><path d="M11 4v14M4 11l7-7 7 7" fill="none" stroke="#fff" stroke-width="3"/></svg>
</div>

</body>
</html>
```